Ridgeway Fruit Depot Logo/Label Design

I am designing a blueberry label that will be placed on clam shells when the fruit is packed. The label will the company name "The Ridgeway Fruit Depot". It will also list Blueberries/Bleuets (Blueberries in French). It small print it would say Dist. By/Par The Ridgeway Fruit Depot, Corliss, GA 30874 USA. It would also list the package size. 1 US Dry Pint/1 Chopine Seche US 551 ml. I have provided some sample labels that other marketers use.

```html
<!DOCTYPE html>
<html lang="en">
<head>
<meta charset="utf-8">
<title>The Ridgeway Fruit Depot – Blueberries Label</title>
<link rel="stylesheet" href="https://fonts.googleapis.com/css2?family=Montserrat:wght@500;800&family=Nunito:ital,wght@1,800&display=swap">
<style>
  :root {
    --label-navy: #474a8a;
    --label-fill: #e6e4f1;
    --label-lilac: #8378bb;
    --label-ink: #2b2a5c;
    --berry-deep: #3b3f86;
    --berry-light: #8d93cf;
    --page-bg: #ffffff;
  }
  html, body {
    margin: 0;
    padding: 0;
    width: 1200px;
    height: 840px;
    overflow: hidden;
    background: var(--page-bg);
  }
  .label-canvas {
    position: relative;
    width: 1200px;
    height: 840px;
  }
  .label-shape {
    position: absolute;
    inset: 0;
  }
  .brand-name {
    position: absolute;
    left: 0;
    width: 1200px;
    top: 104px;
    margin: 0;
    text-align: center;
    font-family: "Montserrat", sans-serif;
    font-weight: 800;
    color: var(--label-navy);
    line-height: 1;
  }
  .brand-name .brand-line {
    display: block;
  }
  .brand-name .brand-small {
    font-size: 22px;
    letter-spacing: 2px;
  }
  .brand-name .brand-large {
    font-size: 40px;
    letter-spacing: 1px;
    margin-top: 8px;
  }
  .brand-name .brand-medium {
    font-size: 24px;
    letter-spacing: 3px;
    margin-top: 8px;
  }
  .product-name {
    position: absolute;
    left: 0;
    width: 1200px;
    top: 458px;
    margin: 0;
    text-align: center;
    font-family: "Montserrat", sans-serif;
    font-weight: 800;
    color: var(--label-navy);
    font-size: 58px;
    line-height: 62px;
    letter-spacing: 1px;
  }
  .product-name span { display: block; }
  .product-rule {
    position: absolute;
    left: 537px;
    top: 597px;
    width: 121px;
    height: 3px;
    background: var(--label-lilac);
  }
  .pack-size {
    position: absolute;
    left: 0;
    width: 1200px;
    top: 622px;
    margin: 0;
    text-align: center;
    font-family: "Nunito", sans-serif;
    font-style: italic;
    font-weight: 800;
    font-size: 22px;
    line-height: 34px;
    color: var(--label-lilac);
  }
  .pack-size span { display: block; }
  .dist-line {
    font-family: "Montserrat", sans-serif;
    font-weight: 500;
    font-size: 17px;
    fill: var(--label-ink);
  }
</style>
</head>
<body>
<main class="label-canvas">
  <svg class="label-shape" width="1200" height="840" viewBox="0 0 1200 840" xmlns="http://www.w3.org/2000/svg">
    <defs>
      <radialGradient id="berry-tone" cx="45%" cy="40%" r="60%">
        <stop offset="0%" stop-color="var(--berry-light)"/>
        <stop offset="100%" stop-color="var(--berry-deep)"/>
      </radialGradient>
      <path id="dist-path" d="M 319 419 A 282 338 0 0 0 883 419"/>
    </defs>
    <rect class="label-tabs" x="247" y="292" width="709" height="258" rx="31" fill="var(--label-navy)"/>
    <ellipse class="label-frame" cx="601" cy="419" rx="317" ry="376" fill="var(--label-navy)"/>
    <ellipse class="label-face" cx="601" cy="419" rx="298" ry="357" fill="var(--label-fill)"/>
    <ellipse class="berry-illustration" role="img" aria-label="Illustration of three ripe blueberries with green leaves"
             cx="601" cy="342" rx="140" ry="106" fill="url(#berry-tone)" opacity="0.85"/>
    <text class="dist-line">
      <textPath href="#dist-path" startOffset="50%" text-anchor="middle" textLength="680" lengthAdjust="spacingAndGlyphs">DIST. BY/PAR: THE RIDGEWAY FRUIT DEPOT, CORLISS, GA 30874 USA</textPath>
    </text>
  </svg>

  <h1 class="brand-name">
    <span class="brand-line brand-small">THE</span>
    <span class="brand-line brand-large">RIDGEWAY</span>
    <span class="brand-line brand-medium">FRUIT DEPOT</span>
  </h1>

  <h2 class="product-name">
    <span>BLUEBERRIES</span>
    <span>BLUETS</span>
  </h2>

  <div class="product-rule"></div>

  <p class="pack-size">
    <span>1 US Dry Pint &nbsp;|&nbsp; 551 ml</span>
    <span>1 Chopine Seche</span>
  </p>
</main>
</body>
</html>
```